Modern design for Bri-mark Labels A4 Flyer

We need a new flyer design for our existing label/sticker manufacturing business. We have been in operation for over 50 years and need to modernise our promotional material in line with our innovative business practises. We are located in the Sydney Metropolitan area but service nationally. We are wholly Australian owned and operated. We manufacture a large array of labels & stickers over a variety of industries: manufacturing, retail, pharmaceutical, logistics, environmental, food and product labelling. We also cater for other "printed matter". We have a newly developed website that we are happy to use as a base for any design work. It displays our logo, colours and numerous photo ideas, as well as heaps of information. We are after a clean, simple, modern, & inviting approach with a "less is better" feel.
All features on our website I can forward to you when requested.
Updates

Project Deadline Extended
Reason: Due to staff absense need to extend the time.

Target Market(s)

Across the board, manufacturing, pharmaceutical, food, marketing etc

Industry/Entity Type

Business

Requirements
Must have
• A4 double sided with the idea of being dual purpose - as an A4 d/s sheet in a presentation folder as well as being able to trifold it into a d/l envelope for mailouts.
Logo
Association with our website - colours - www.brimarklabels.com.au
More pics/photos than text
Our slogan :" For quality and service that really stick"
Our QR code
Contact details very accessible
Testimonials
Nice to have
• On our website is a peelback sticker of our logo
Your ideas appreciated.
Full colour
Should not have
• Comics
Anything "old school"

```html
<!DOCTYPE html>
<html lang="en">
<head>
<meta charset="utf-8">
<title>Bri-mark Labels – Flyer</title>
<link rel="stylesheet" href="https://fonts.googleapis.com/css2?family=Open+Sans:ital,wght@0,300;0,400;1,300&family=Tinos&display=swap">
<style>
  :root {
    --red: #e8392c;
    --red-deep: #d42a20;
    --red-light: #f25a45;
    --amber: #f7a823;
    --orange: #f38b22;
    --charcoal: #262626;
    --charcoal-2: #303030;
    --charcoal-3: #1f1f1f;
    --white: #ffffff;
    --ink: #333333;
    --serif: "Tinos", "Times New Roman", serif;
    --sans: "Open Sans", Arial, sans-serif;
  }
  * { box-sizing: border-box; margin: 0; padding: 0; }
  html, body { width: 1200px; height: 848px; overflow: hidden; background: var(--white); }
  .flyer { position: relative; width: 1200px; height: 848px; }
  .cell { position: absolute; }
  .col-a { left: 0; width: 386px; }
  .col-b { left: 386px; width: 415px; }
  .col-c { left: 801px; width: 399px; }
  .row-top { top: 0; height: 227px; }
  .row-mid { top: 227px; height: 277px; }
  .row-low { top: 504px; height: 258px; }

  .photo-red-a { background: radial-gradient(circle at 40% 60%, var(--red-light), var(--red-deep)); }
  .photo-red-b { background: linear-gradient(160deg, var(--red-light), var(--red) 55%, var(--red-deep)); }
  .photo-red-c { background: radial-gradient(circle at 70% 40%, #f46a4e, var(--red)); }
  .photo-dark-a { background: radial-gradient(circle at 45% 50%, #3a3a3a, var(--charcoal-3)); }
  .photo-dark-b { background: radial-gradient(circle at 55% 45%, #3d3d3d, var(--charcoal)); }
  .photo-dark-c { background: radial-gradient(circle at 50% 40%, #333, var(--charcoal-3)); }

  .brand-badge {
    position: absolute; top: 39px; width: 94px; height: 94px; border-radius: 50%;
    background: var(--white); display: flex; align-items: center; justify-content: center;
    text-align: center; font-family: var(--serif); font-size: 15px; line-height: 1.1;
    color: var(--red-deep);
  }

  .intro-heading { position: absolute; top: 152px; left: 386px; width: 415px; text-align: center; color: var(--white); font-family: var(--serif); }
  .intro-heading .kicker { font-size: 13px; letter-spacing: 0.3px; }
  .intro-heading .headline { font-size: 32px; line-height: 1.05; letter-spacing: 0.5px; }

  .about { background: var(--amber); padding: 44px 18px 0 22px; color: var(--white); font-family: var(--sans); font-weight: 300; font-size: 12.3px; line-height: 1.33; }
  .about p + p { margin-top: 12px; }

  .testimonial { background: var(--orange); padding: 30px 38px 0 38px; color: var(--white); }
  .testimonial .kicker { font-family: var(--serif); font-size: 13px; }
  .testimonial .headline { font-family: var(--serif); font-size: 29px; line-height: 1; letter-spacing: 0.4px; }
  .testimonial blockquote { margin-top: 18px; font-family: var(--sans); font-style: italic; font-weight: 300; font-size: 14px; line-height: 1.3; }
  .testimonial .signoff { margin-top: 40px; font-family: var(--sans); font-weight: 300; font-size: 11px; line-height: 1.3; }

  .services { background: var(--amber); padding: 36px 0 0 66px; display: flex; gap: 0; }
  .services ul { list-style: none; font-family: var(--serif); font-size: 12.5px; color: var(--white); }
  .services ul:first-child { width: 170px; }
  .services li { height: 22.8px; position: relative; }
  .services li::before { content: ""; position: absolute; left: -16px; top: 6px; width: 4px; height: 4px; border-radius: 50%; background: var(--white); }

  .slogan { position: absolute; top: 118px; width: 100%; text-align: center; color: var(--white); font-family: var(--serif); }
  .slogan .kicker { font-size: 13px; }
  .slogan .headline { font-size: 29px; line-height: 1.05; letter-spacing: 0.3px; }

  .footer { position: absolute; top: 762px; height: 86px; background: var(--white); }
  .footer .url { display: block; text-align: center; margin-top: 9px; font-family: var(--sans); font-size: 13px; color: var(--ink); text-decoration: none; }
</style>
</head>
<body>
<main class="flyer">
  <div class="cell col-a row-top photo-red-a" role="img" aria-label="Red-toned photo of printed product labels on containers"></div>
  <div class="cell col-b row-top photo-red-b" role="img" aria-label="Red-toned photo of a labelled bottle close-up"></div>
  <div class="cell col-c row-top photo-red-c" role="img" aria-label="Red-toned photo of a nutrition panel label"></div>

  <div class="brand-badge" style="left:131px">Bri-mark<br>Labels</div>
  <div class="brand-badge" style="left:541px">Bri-mark<br>Labels</div>
  <div class="brand-badge" style="left:961px">Bri-mark<br>Labels</div>

  <div class="intro-heading">
    <div class="kicker">NEED CUSTOMISED</div>
    <div class="headline">LABELS OR STICKERS?</div>
  </div>

  <section class="cell col-a row-mid about">
    <p>Our focus is aimed at being able to best serve our clients’ needs.</p>
    <p>Bri-mark Labels was formed in 1963 to serve businesses on Sydney’s north shore with effective labelling solutions. Over the last almost 50 years the client base has stretched across the country and across industry sectors, although the northern beaches is still our base.</p>
  </section>

  <section class="cell col-b row-mid testimonial">
    <div class="kicker">WHAT</div>
    <div class="headline">OTHERS ARE SAYING…</div>
    <blockquote>The team at Bri-mark Labels have always responded quickly to our requirements and kept me informed of progress. I cannot fault their customer service and willingness to help.</blockquote>
    <div class="signoff">Regards,<br>Mara Lenton,<br>Customer Support Manager<br>Norvale - South East Asia Pacific</div>
  </section>

  <section class="cell col-c row-mid services">
    <ul>
      <li>Printed or unprinted</li><li>Special effects</li><li>4 colour process</li><li>Varnishing</li><li>Foil stamping</li><li>Despatch</li><li>Laminating</li><li>Barcode</li><li>Perforated</li><li>Numbered</li>
    </ul>
    <ul>
      <li>Back slit</li><li>Variable information</li><li>Die cutting</li><li>Motor vehicle</li><li>Bumper stickers</li><li>Environmental</li><li>Recycling</li><li>Chemical</li><li>Promotional</li><li>QR Codes</li>
    </ul>
  </section>

  <div class="cell col-a row-low photo-dark-a" role="img" aria-label="Dark monochrome photo of a nutrition facts label beside fruit">
    <div class="slogan"><div class="kicker">FOR QUALITY AND SERVICE</div><div class="headline">THAT REALLY STICK</div></div>
  </div>
  <div class="cell col-b row-low photo-dark-b" role="img" aria-label="Dark monochrome photo of a blank from/to address label"></div>
  <div class="cell col-c row-low photo-dark-c" role="img" aria-label="Dark monochrome photo of a product label on a package">
    <div class="slogan"><div class="kicker">FOR QUALITY AND SERVICE</div><div class="headline">THAT REALLY STICK</div></div>
  </div>

  <footer class="footer col-a"><a class="url" href="#">www.brimarklabels.com.au</a></footer>
  <footer class="footer col-b"><a class="url" href="#">www.brimarklabels.com.au</a></footer>
  <footer class="footer col-c"><a class="url" href="#">www.brimarklabels.com.au</a></footer>
</main>
</body>
</html>
```